Spice Rum label design for 288° Craft Distillery

We would like a label designed for our Spiced Rum. We would like to name it "Willow Cove Spiced Rum" or something very similar to that. The name of our distillery is "288° Craft Distillery". We would like our logo on the top right of our label, maybe at a nickel or quarter size and in a different color. We would like this label to be in compliance with the State and Federal regulations regarding liquor, specifically spiced rum. We do not yet have a full ingredient statement but it will include vanilla, cinnamon and other natural flavors.
Attached is a farmer lady, so maybe something similar to this but a bit more classy/upscale. Our distillery is located right next to Pine Hollow Lake, a 3600 acre lake, please include a beach/lake in the design. Our distillery has a roof top bar and you can watch the activities of the lake from our roof top, so the lake is very important to us.
We are second and third generation chemist and I have my master in Food Science so these technologies are also important to us. But the focus should be on "Willow Cove" which is a specific beach on Pine Hollow Lake.

Target Market(s)

Target market is both male and female drinkers of rum

Font styles to use
Decorative
Script

Requirements
Must have
• Must have our logo along with Spiced Rum and Willow Cove
Nice to have
• design of a farmer lady next to a beautiful beach. Maybe on a lawn chair or next to a fence? Maybe a sunsetting or a sailboat in the background?

```html
<!DOCTYPE html>
<html lang="en">
<head>
<meta charset="utf-8">
<title>Willow Cove Spiced Rum – Label</title>
<link href="https://fonts.googleapis.com/css2?family=Oswald:wght@400&family=Roboto+Condensed:wght@400;700;800&family=Yellowtail&family=Homemade+Apple&display=swap" rel="stylesheet">
<style>
  :root{
    --backdrop:#c9d6dc;
    --label-blue:#7fa0b0;
    --label-blue-soft:#8aaabb;
    --ink:#1d2327;
    --cream:#ece4d4;
    --cream-line:#8c7f6a;
    --seal:#9c9385;
  }
  *{margin:0;padding:0;box-sizing:border-box}
  html,body{width:1200px;height:1200px;overflow:hidden}
  body{background:var(--backdrop);position:relative;font-family:"Roboto Condensed",sans-serif;color:var(--ink)}
  .label{position:absolute;left:220px;top:175px;width:760px;height:850px;background:var(--label-blue);overflow:hidden}
  .label > *{position:absolute}

  .distillery-name{left:0;right:0;top:34px;text-align:center;font-family:"Roboto Condensed",sans-serif;font-weight:800;color:var(--ink);line-height:1}
  .distillery-name .figure{display:block;font-size:96px;letter-spacing:1px}
  .distillery-name .words{display:block;font-size:40px;letter-spacing:4px;margin-top:14px}
  .distillery-seal{left:590px;top:60px;width:96px;height:96px;border-radius:50%;background:var(--seal)}

  .product-name{left:0;right:0;top:242px;text-align:center;font-family:"Oswald",sans-serif;font-weight:400;font-size:112px;line-height:1;color:var(--cream);letter-spacing:-1px}
  .product-type{left:0;right:0;top:366px;text-align:center;font-weight:800;font-size:64px;line-height:1}
  .flavor-note{left:0;right:0;top:455px;text-align:center;font-size:14px;font-weight:700;letter-spacing:.3px;color:#2b3438}
  .origin-script{left:0;right:0;top:490px;text-align:center;font-family:"Yellowtail",cursive;font-size:32px;line-height:1.1}

  .botanicals-mark{left:52px;top:392px;width:104px;height:104px;border-radius:50%;border:3px solid var(--label-blue-soft)}
  .batch-panel{left:115px;top:575px;width:540px;height:200px}
</style>
</head>
<body>
<div class="label">
  <div class="distillery-name">
    <span class="figure">288°</span>
    <span class="words">CRAFT DISTILLERY</span>
  </div>
  <div class="distillery-seal" aria-hidden="true"></div>

  <div class="product-name">WILLOW COVE</div>
  <div class="product-type">SPICED RUM</div>
  <div class="flavor-note">INCLUDE VANILLA, CINNAMON AND OTHER NATURAL FLAVORS</div>
  <div class="origin-script">Hand Crafted in the Heart of<br>Pine Hollow Lake Iowa</div>

  <div class="botanicals-mark" aria-hidden="true"></div>

  <svg class="batch-panel" viewBox="0 0 540 200">
    <polygon points="24,0 516,0 540,24 540,176 516,200 24,200 0,176 0,24" fill="#ece4d4"/>
    <polygon points="30,8 510,8 532,30 532,170 510,192 30,192 8,170 8,30" fill="none" stroke="#8c7f6a" stroke-width="2"/>
    <text x="270" y="38" text-anchor="middle" font-family="Roboto Condensed, sans-serif" font-weight="700" font-size="17" fill="#1d2327">HANDCRAFTED IN SMALL BATCHES</text>
    <circle cx="70" cy="90" r="30" fill="none" stroke="#8c7f6a" stroke-width="2"/>
    <g font-family="Roboto Condensed, sans-serif" font-size="13" fill="#1d2327">
      <text x="118" y="82">BATCH:</text>
      <text x="118" y="104">DATE:</text>
      <text x="290" y="80">BOTTLE:</text>
      <text x="290" y="104">DISTILLER:</text>
    </g>
    <g stroke="#1d2327" stroke-dasharray="2 2" stroke-width="1">
      <line x1="162" y1="84" x2="262" y2="84"/>
      <line x1="152" y1="106" x2="262" y2="106"/>
      <line x1="340" y1="82" x2="432" y2="82"/>
      <line x1="352" y1="106" x2="440" y2="106"/>
    </g>
    <g font-family="Homemade Apple, cursive" font-size="10" fill="#2b3438">
      <text x="170" y="81">A-2/021</text>
      <text x="158" y="103">04 / 06 / 2020</text>
      <text x="352" y="79">025/250</text>
      <text x="355" y="103">Avery Lindqvist</text>
    </g>
    <circle cx="475" cy="90" r="30" fill="none" stroke="#8c7f6a" stroke-width="2"/>
    <g font-family="Roboto Condensed, sans-serif" text-anchor="middle" fill="#1d2327">
      <text x="270" y="138" font-size="9.5" font-weight="700">REGIONAL HIGH QUALITY RUM FROM</text>
      <text x="270" y="150" font-size="9.5" font-weight="700">PINE HOLLOW LAKE WITH 14 HAND PICKED BOTANICALS</text>
      <text x="270" y="164" font-size="9">PRODUCED AND BOTTLED by 288 Craft Distillery LLC</text>
      <text x="270" y="176" font-size="9">418 SHORELINE DRIVE, PINE HOLLOW LAKE, IA, 50612, USA</text>
    </g>
    <text x="36" y="164" font-family="Roboto Condensed, sans-serif" font-size="14" fill="#1d2327">46 % ALC/VOL.</text>
    <text x="504" y="164" text-anchor="end" font-family="Roboto Condensed, sans-serif" font-size="14" fill="#1d2327">700 ML</text>
  </svg>
</div>
</body>
</html>
```